依頼詳細
こちらのファッションアイテム検索ページ( http://www.furelo.example/item/ )にカテゴリーがあるのですが、各カテゴリーを象徴するアイコンと、各コンテンツを象徴するアイコンを制作お願いしたいと思います。 サイトと現在開発中のiPhoneアプリにて使用します。
記載項目
以下カテゴリーがあるので各カテゴリーを象徴するアイコンを制作お願いしたいと思います。
iPhoneで32pxくらいのサイズを最小サイズとして使用予定なので視認性の高いアイコンを希望します。
+コンテスト
+ブランド
+コーディネート
+ アウター
+ トップス
+ ワンピース・ドレス
+ スカート
+ パンツ
+ レッグウェア
+ 靴
+ バッグ
+ アクセサリー
+ ヘアアクセサリー
+ 帽子
+ 服飾系小物
+ ルーム・アンダーウェア
+ コスメ・ビューティ
+ 雑貨・小物
+ 水着・浴衣
+ その他
+ 背景・イラスト
+ テキスト
+ フレーム
希望イメージ
シンプル 複雑
単色 カラフル
暗い 明るい
日常 高級
遊び心 厳粛
未来的 伝統的
女性的 男性的
希望する色
納品ファイル
• イラストレーター形式 (.ai)
補足説明

```html
<!DOCTYPE html>
<html lang="ja">
<head>
<meta charset="utf-8">
<title>カテゴリー一覧</title>
<link href="https://fonts.googleapis.com/css2?family=Noto+Sans+JP:wght@400;500&display=swap" rel="stylesheet">
<style>
  :root {
    --bg: #f9dfdf;
    --status: #0a0a0a;
    --title-top: #5a5a5a;
    --title-bottom: #2b2b2b;
    --title-text: #ffffff;
    --row-line: #c9b9b9;
    --label: #c8336f;
    --arrow: #e0107c;
    --icon-bg: #d9d3d3;
    --icon-fill: #d42a5e;
  }
  * { margin: 0; padding: 0; box-sizing: border-box; }
  html, body {
    width: 1200px; height: 2224px; overflow: hidden;
    background: var(--bg);
    font-family: "Noto Sans JP", sans-serif;
  }
  .screen { position: relative; width: 1200px; height: 2224px; background: var(--bg); }
  .status-bar {
    height: 80px; background: var(--status);
    display: flex; justify-content: flex-end; align-items: center;
    gap: 22px; padding-right: 28px; color: #fff;
  }
  .status-bar .clock { font-size: 48px; font-weight: 500; }
  .title-bar {
    height: 152px;
    background: linear-gradient(var(--title-top), var(--title-bottom));
    border-radius: 0 0 16px 16px;
    display: flex; justify-content: center; align-items: center;
    color: var(--title-text); font-size: 64px; font-weight: 400;
  }
  .category-list {
    list-style: none;
    position: absolute; left: 56px; top: 276px; width: 1064px;
    border-top: 3px solid var(--row-line);
  }
  .category-item {
    height: 150px; display: flex; align-items: center;
    border-bottom: 3px solid var(--row-line);
  }
  .category-icon {
    width: 120px; height: 120px; margin-left: 16px;
    background: var(--icon-bg); border: 2px solid #a9a0a0;
    display: flex; justify-content: center; align-items: center;
  }
  .category-icon span {
    width: 84px; height: 84px; background: var(--icon-fill); border-radius: 10px;
  }
  .category-label {
    margin-left: 140px; flex: 1;
    color: var(--label); font-size: 50px; letter-spacing: 1px;
  }
  .category-arrow { margin-right: 56px; }
</style>
</head>
<body>
<div class="screen">
  <div class="status-bar">
    <svg width="56" height="44" viewBox="0 0 56 44" aria-label="Wi-Fi">
      <path d="M4 16 A36 36 0 0 1 52 16" stroke="#fff" stroke-width="6" fill="none"/>
      <path d="M14 26 A22 22 0 0 1 42 26" stroke="#fff" stroke-width="6" fill="none"/>
      <circle cx="28" cy="38" r="5" fill="#fff"/>
    </svg>
    <svg width="52" height="44" viewBox="0 0 52 44" aria-label="電波">
      <rect x="0" y="32" width="8" height="12" fill="#fff"/>
      <rect x="14" y="24" width="8" height="20" fill="#fff"/>
      <rect x="28" y="14" width="8" height="30" fill="#fff"/>
      <rect x="42" y="4" width="8" height="40" fill="#fff"/>
    </svg>
    <svg width="76" height="40" viewBox="0 0 76 40" aria-label="バッテリー">
      <rect x="2" y="4" width="66" height="32" rx="4" stroke="#fff" stroke-width="4" fill="none"/>
      <rect x="70" y="14" width="6" height="12" fill="#fff"/>
      <rect x="8" y="10" width="54" height="20" fill="#fff"/>
    </svg>
    <span class="clock">19:02</span>
  </div>

  <header class="title-bar">Title</header>

  <ul class="category-list">
    <li class="category-item"><div class="category-icon" role="img" aria-label="コンテストのアイコン（王冠）"><span></span></div><span class="category-label">+コンテスト</span><svg class="category-arrow" width="40" height="64" viewBox="0 0 40 64"><path d="M0 0 L40 32 L0 64 Z" fill="var(--arrow)"/></svg></li>
    <li class="category-item"><div class="category-icon" role="img" aria-label="ブランドのアイコン（Bマークの服）"><span></span></div><span class="category-label">+ブランド</span><svg class="category-arrow" width="40" height="64" viewBox="0 0 40 64"><path d="M0 0 L40 32 L0 64 Z" fill="var(--arrow)"/></svg></li>
    <li class="category-item"><div class="category-icon" role="img" aria-label="コーディネートのアイコン（服の組み合わせ）"><span></span></div><span class="category-label">+コーディネート</span><svg class="category-arrow" width="40" height="64" viewBox="0 0 40 64"><path d="M0 0 L40 32 L0 64 Z" fill="var(--arrow)"/></svg></li>
    <li class="category-item"><div class="category-icon" role="img" aria-label="アウターのアイコン（コート）"><span></span></div><span class="category-label">+ アウター</span><svg class="category-arrow" width="40" height="64" viewBox="0 0 40 64"><path d="M0 0 L40 32 L0 64 Z" fill="var(--arrow)"/></svg></li>
    <li class="category-item"><div class="category-icon" role="img" aria-label="トップスのアイコン（ニット）"><span></span></div><span class="category-label">+ トップス</span><svg class="category-arrow" width="40" height="64" viewBox="0 0 40 64"><path d="M0 0 L40 32 L0 64 Z" fill="var(--arrow)"/></svg></li>
    <li class="category-item"><div class="category-icon" role="img" aria-label="ワンピース・ドレスのアイコン"><span></span></div><span class="category-label">+ ワンピース・ドレス</span><svg class="category-arrow" width="40" height="64" viewBox="0 0 40 64"><path d="M0 0 L40 32 L0 64 Z" fill="var(--arrow)"/></svg></li>
    <li class="category-item"><div class="category-icon" role="img" aria-label="スカートのアイコン"><span></span></div><span class="category-label">+ スカート</span><svg class="category-arrow" width="40" height="64" viewBox="0 0 40 64"><path d="M0 0 L40 32 L0 64 Z" fill="var(--arrow)"/></svg></li>
    <li class="category-item"><div class="category-icon" role="img" aria-label="パンツのアイコン"><span></span></div><span class="category-label">+ パンツ</span><svg class="category-arrow" width="40" height="64" viewBox="0 0 40 64"><path d="M0 0 L40 32 L0 64 Z" fill="var(--arrow)"/></svg></li>
    <li class="category-item"><div class="category-icon" role="img" aria-label="レッグウェアのアイコン（靴下）"><span></span></div><span class="category-label">+ レッグウェア</span><svg class="category-arrow" width="40" height="64" viewBox="0 0 40 64"><path d="M0 0 L40 32 L0 64 Z" fill="var(--arrow)"/></svg></li>
    <li class="category-item"><div class="category-icon" role="img" aria-label="靴のアイコン（パンプス）"><span></span></div><span class="category-label">+ 靴</span><svg class="category-arrow" width="40" height="64" viewBox="0 0 40 64"><path d="M0 0 L40 32 L0 64 Z" fill="var(--arrow)"/></svg></li>
    <li class="category-item"><div class="category-icon" role="img" aria-label="バッグのアイコン"><span></span></div><span class="category-label">+バッグ</span><svg class="category-arrow" width="40" height="64" viewBox="0 0 40 64"><path d="M0 0 L40 32 L0 64 Z" fill="var(--arrow)"/></svg></li>
    <li class="category-item"><div class="category-icon" role="img" aria-label="アクセサリーのアイコン（ネックレス）"><span></span></div><span class="category-label">+ アクセサリー</span><svg class="category-arrow" width="40" height="64" viewBox="0 0 40 64"><path d="M0 0 L40 32 L0 64 Z" fill="var(--arrow)"/></svg></li>
  </ul>
</div>
</body>
</html>
```